Harbor Mortgage Relief

Please help us give our website a remake or a FACELIFT. It is not very good but it says what we need it to say. But the design is terrible.
I would like our new design font and logo to be used as the theme.

I also want more photos on the site.

I also want consistency with the pages so they look clean.

We want the professionals to do this, let's see what you got!

Thank you!
Updates

Project Deadline Extended
Reason: I can understand you want to be paid. So I will commit to the fee but I want you to have time to make a KICK ASS website for me dudes! Thanks

HI!  Just wanted to say thanks for your time on these.  A lot are great.  However the firefighters have nothing to do with Foreclosure.  We are saving peoples homes from the bank taking them and selling them.   I LOVE the house photos and the families on the website.  That is the direction we like.  THanks.

THANK U ALL FOR THE WORK!   I like a few ending in the numbers: 147  733  693  536  620  478  727  508     I will go over them and choose one soon.  Thank you.   You will be paid shortly. 

Requirements
Must have
• Bright, Upbeat photos. Color scheme should be in order. We like icons on the bottom. not just text.

```html
<!DOCTYPE html>
<html lang="en">
<head>
<meta charset="utf-8">
<title>Harbor Mortgage Relief</title>
<link href="https://fonts.googleapis.com/css2?family=Montserrat:wght@400;500;600;700&display=swap" rel="stylesheet">
<style>
:root{
  --red:#e3141c;
  --red-dark:#b80d13;
  --ink:#3d3d3d;
  --text:#555;
  --page:#e4e4e4;
  --header:#f1efeb;
  --panel:#fff;
  --soft:#f0f0f0;
  --sky:#8fc8ea;
  --navy:#173450;
  --quote:#fff;
  --footer:#2c2c2c;
  --footer-text:#e8e8e8;
}
*{box-sizing:border-box;margin:0;padding:0}
html,body{width:1133px;height:1200px;overflow:hidden}
body{position:relative;background:var(--page);font-family:"Montserrat",Arial,sans-serif;color:var(--text)}
.header-band{position:absolute;left:0;top:0;width:1133px;height:147px;background:var(--header)}
.brand{position:absolute;left:134px;top:34px;display:flex;align-items:center;gap:12px}
.brand-dot{width:56px;height:56px;border-radius:50%;background:var(--red)}
.brand-name{font-weight:700;font-size:22px;line-height:26px;color:var(--red);text-transform:uppercase;width:200px}
.language{position:absolute;left:627px;top:28px;font-weight:700;font-size:15px;color:#1e1e1e;letter-spacing:.3px}
.call{position:absolute;left:803px;top:22px;display:flex;gap:9px}
.call-icon{width:32px;height:32px;border-radius:5px;background:var(--red);display:flex;align-items:center;justify-content:center}
.call-label{font-size:13px;font-weight:500;color:#1e1e1e;line-height:14px;margin-top:2px}
.call-number{font-size:24px;color:var(--red);line-height:28px}
.nav{position:absolute;left:438px;top:75px;width:565px;height:30px;background:linear-gradient(var(--red),var(--red-dark));border-radius:3px;display:flex}
.nav a{display:flex;align-items:center;justify-content:center;color:#fff;text-decoration:none;font-size:13px;font-weight:500;height:100%;border-right:1px solid #8e0a0f}
.nav a:last-child{border-right:0}
.panel{position:absolute;left:133px;top:114px;width:870px;height:872px;background:var(--panel);border-radius:5px;box-shadow:0 0 3px rgba(0,0,0,.15)}
.hero{position:absolute;left:142px;top:123px;width:852px;height:315px;border-radius:4px;background:linear-gradient(180deg,#8fa9b8 0%,#6e7d6a 45%,#c79a62 75%,#7d7b72 100%)}
.welcome{position:absolute;left:151px;top:455px;font-size:18.5px;font-weight:600;color:var(--ink);letter-spacing:.2px}
.welcome em{font-style:normal;color:var(--red)}
.intro{position:absolute;left:151px;top:492px;width:602px;font-size:12.6px;line-height:20.4px;color:var(--text)}
.intro p+p{margin-top:20px}
.read-more{position:absolute;left:151px;top:701px;font-size:11.5px;color:var(--red);text-decoration:none}
.options{position:absolute;left:150px;top:731px;width:600px;height:240px;background:var(--soft);border-radius:4px;padding:10px 20px}
.options h2{font-size:12.6px;font-weight:600;color:#444;line-height:16px;width:520px;margin-left:-1px}
.options ul{list-style:none;margin-top:10px}
.options li{position:relative;padding-left:21px;font-size:12.8px;line-height:15.5px;color:var(--text);margin-bottom:9.5px;width:490px}
.options li::before{content:"";position:absolute;left:3px;top:4px;border-left:6px solid #aaa;border-top:4px solid transparent;border-bottom:4px solid transparent}
.testimonials{position:absolute;left:774px;top:457px;width:220px;height:490px;background:var(--sky);border-radius:4px;padding:10px 13px}
.testimonials h2{font-size:18.5px;font-weight:600;color:var(--navy);margin-bottom:9px}
.quote{position:relative;padding-left:28px;margin-bottom:13px}
.quote::before{content:"\201C";position:absolute;left:0;top:-8px;font-size:44px;line-height:50px;color:var(--quote);font-family:Georgia,serif}
.quote p{font-size:11.6px;line-height:16px;color:#fff}
.quote cite{display:block;font-style:normal;font-size:11px;color:var(--navy);margin-top:5px}
.footer{position:absolute;left:0;top:1012px;width:1133px;height:188px;background:var(--footer);border-top:3px solid var(--red)}
.mail-art{position:absolute;left:221px;top:1037px;width:76px;height:65px;border-radius:6px;background:linear-gradient(135deg,#f2a93b 0 30%,#39a6d4 30% 100%)}
.footer-email{position:absolute;left:133px;top:1108px;font-size:12.5px;color:var(--footer-text)}
.footer-title{position:absolute;font-size:12.5px;font-weight:500;color:var(--footer-text)}
.signup-field{position:absolute;left:424px;top:1065px;width:172px;height:23px;border-radius:4px;background:#8a8a8a;color:#eee;font-size:11px;padding:5px 8px}
.signup-button{position:absolute;left:424px;top:1097px;width:52px;height:25px;border-radius:3px;background:linear-gradient(#fafafa,#cfcfcf);color:#333;font-size:14px;text-align:center;line-height:25px}
.social{position:absolute;top:1065px;width:28px;height:28px;border-radius:3px}
.social-one{left:642px;background:#5bbbe6}
.social-two{left:680px;background:#3d5f9f}
.social-three{left:717px;background:#1f77a8}
.address{position:absolute;left:784px;top:1043px;font-size:12.5px;line-height:20.4px;color:var(--footer-text)}
.rule{position:absolute;left:133px;top:1153px;width:870px;height:1px;background:#464646}
.copyright{position:absolute;left:0;top:1170px;width:1133px;text-align:center;font-size:10.5px;color:#8e8e8e}
</style>
</head>
<body>
<div class="header-band"></div>
<div class="brand"><span class="brand-dot"></span><span class="brand-name">Harbor Mortgage Relief</span></div>
<div class="language">HABLAMOS ESPANOL</div>
<div class="call">
  <div class="call-icon">
    <svg width="18" height="18" viewBox="0 0 24 24"><path fill="#fff" d="M6.6 10.8a15 15 0 0 0 6.6 6.6l2.2-2.2c.3-.3.7-.4 1-.2 1.1.4 2.3.6 3.6.6.6 0 1 .4 1 1V20c0 .6-.4 1-1 1A17 17 0 0 1 3 4c0-.6.4-1 1-1h3.5c.6 0 1 .4 1 1 0 1.3.2 2.5.6 3.6.1.3 0 .7-.2 1z"/></svg>
  </div>
  <div><div class="call-label">CALL TOLL FREE NOW</div><div class="call-number">800-555-0147</div></div>
</div>
<nav class="nav">
  <a href="#" style="width:82px">HOME</a>
  <a href="#" style="width:101px">ABOUT US</a>
  <a href="#" style="width:99px">SERVICES</a>
  <a href="#" style="width:118px">CONTACT US</a>
  <a href="#" style="width:165px">OWNER OPTIONS</a>
</nav>

<div class="panel"></div>
<div class="hero" role="img" aria-label="Smiling family of four in front of a lit suburban house at dusk"></div>

<h1 class="welcome">WELCOME TO <em>HARBOR</em> MORTGAGE <em>RELIEF</em></h1>
<div class="intro">
  <p>HARBOR MORTGAGE RELIEF specializes in assisting homeowners who are in FORECLOSURE, by offering solid alternatives to losing your home in a Trustee Sale. Having your home foreclosed on can damage your credit for up to 7 years. Most foreclosures end with the home owner being evicted from their home, leaving them with no money, no place to live and without ample time to safely remove their possessions from their home. There is no need to have this happen to you. No matter what part of foreclosure process you are in, WE CAN HELP!</p>
  <p>If you have received a Notice of Default (NOD) or Notice of Trustee Sale (NTS), you have options. Contact us today to speak to one of our licensed specialist, and let us help you put this situation behind you.</p>
</div>
<a class="read-more" href="#">Read more</a>

<section class="options">
  <h2>You may not know it but there are several great options available to you. We can help you determine which one will work best for you FREE OF CHARGE:</h2>
  <ul>
    <li>Bringing your mortgage current to stop the foreclosure</li>
    <li>HMR can purchase your home with CASH in 7-10 days</li>
    <li>Financing/Purchase Options</li>
    <li>Relocations Assistance - if needed</li>
    <li>Remodel your home to increase it's value</li>
    <li>Many other options are available - We realize that all of our clients have different needs. We look at your individual needs to customize a solution just for you.</li>
  </ul>
</section>

<aside class="testimonials">
  <h2>Testimonials</h2>
  <div class="quote">
    <p>I'd like to express my gratitude to you and your company and I have to add, for all of the trustworthy and reliable service that you bring to the public. Your company helped put me back together, you in particular are wesome! Thank you again Tom.</p>
    <cite>Dana</cite>
  </div>
  <div class="quote">
    <p>Harbor Mortgage Relief has been an absolute life saver for me and my family. Their services have changed everything. Instead of my house going into foreclosure and losing everything I own, I now have a chance to start over and the money to do it with! They've been fast, friendly and efficient. I would recommend their services to anyone facing foreclosure.</p>
    <cite>Rachel T.</cite>
  </div>
</aside>

<footer class="footer"></footer>
<div class="mail-art" role="img" aria-label="Illustrated envelope with a flying note"></div>
<div class="footer-email">INFO@HARBORMORTGAGERELIEF.COM</div>
<div class="footer-title" style="left:424px;top:1043px">JOIN OUR MAILING LIST</div>
<div class="signup-field">Your e-mail address</div>
<div class="signup-button">Join</div>
<div class="footer-title" style="left:641px;top:1043px">FOLLOW US</div>
<span class="social social-one"></span>
<span class="social social-two"></span>
<span class="social social-three"></span>
<div class="address">HARBOR MORTGAGE RELIEF<br>218 Harbor View Suite 300<br>Bayport, CA 90000<br>800-555-0147</div>
<div class="rule"></div>
<div class="copyright">© 2012. HARBORMORTGAGERELIEF.COM. All rights reserved. &nbsp;Reserved | Privacy Policy</div>
</body>
</html>
```